Dental clinic brochure design (Z fold)

We need a new brochure design made for our dental clinic - Brackenfold Dental Surgery. One side is in English, the other is in Vietnamese - all text and translations provided in brochure sample with further instructions in word doc. We require a brochure design in a Z fold to convey a family friendly dental clinic, incorporating our logo colour into the theme and designers choice on complimentary colours. Additional high quality images are provided for use if required or free to use own images.

Colors
33b8a4
00a990
86cfc6

Requirements
Must have
• Easy to read font, flows from text to pictures and page to page
• At least 2 dental images

```html
<!DOCTYPE html>
<html lang="en">
<head>
<meta charset="utf-8">
<title>Brackenfold Dental Surgery – Brochure</title>
<link href="https://fonts.googleapis.com/css2?family=Cinzel:wght@400;600&family=Marcellus+SC&family=Lora:wght@400&family=Open+Sans:wght@400&display=swap" rel="stylesheet">
<style>
  :root{
    --teal:#33b8a4;
    --teal-deep:#00a990;
    --teal-soft:#86cfc6;
    --teal-pale:#d9f0ec;
    --ink:#3d3d3d;
    --plum:#7a3f8f;
    --page:#ffffff;
    --stage:#e9eef0;
  }
  *{box-sizing:border-box;margin:0;padding:0}
  html,body{width:1200px;height:900px;overflow:hidden;background:var(--stage)}
  .brochure{position:absolute;left:30px;top:47px;width:1140px;height:806px;background:var(--page);overflow:hidden;box-shadow:0 4px 18px rgba(0,0,0,.12);font-family:"Marcellus SC",serif;color:var(--ink)}
  .panel{position:absolute;top:0;width:380px;height:806px}
  .panel--left{left:0}
  .panel--middle{left:380px}
  .panel--right{left:760px}
  .photo{position:absolute}
  .band{position:absolute;background:var(--teal-soft);color:#2f3d3b;display:flex;align-items:center;justify-content:center;text-align:center;letter-spacing:1px;font-weight:400}
  .rule{position:absolute;height:1.5px;background:var(--teal-deep)}

  /* left */
  .photo--toddlers{left:0;top:0;width:380px;height:250px;background:linear-gradient(90deg,#fdfdfd,#f1ebe6 40%,#f6f2ee 70%,#fdfdfd)}
  .band--child{left:0;top:250px;width:380px;height:78px;font-size:24px;line-height:1.1}
  .child-copy{position:absolute;left:36px;top:348px;width:310px;font-size:15px;line-height:1.6;text-align:justify;letter-spacing:.4px}
  .child-copy + .child-copy{top:470px}
  .child-copy strong{font-family:"Cinzel",serif;font-weight:600}
  .child-copy .phone{font-family:"Cinzel",serif;font-weight:600;font-size:18px}

  /* middle */
  .photo--smile{left:0;top:0;width:380px;height:190px;background:linear-gradient(180deg,#e7b8a9,#d99c8c 45%,#f3ede8 60%,#c98a7c)}
  .band--treat{left:0;top:190px;width:380px;height:40px;font-size:21px}
  .treatments{position:absolute;left:22px;top:244px;width:350px;display:grid;grid-template-columns:1fr 1.55fr;gap:6px 10px;list-style:none;font-size:14px}
  .treatments li{display:flex;align-items:center;gap:7px}
  .treatments svg{flex:none}
  .band--promo{left:20px;top:354px;width:345px;height:38px;font-size:21px}
  .promo-copy{position:absolute;left:30px;top:404px;width:330px;font-size:14px;line-height:1.5}
  .promo-copy strong{font-family:"Cinzel",serif;font-weight:600;font-size:16px}
  .promo-note{position:absolute;left:30px;top:534px;font-family:"Open Sans",sans-serif;font-size:10px}

  /* lower photo strip */
  .photo--kids{left:0;top:615px;width:640px;height:191px;background:linear-gradient(180deg,#bfe5df,#5fb3a6 55%,#3f9487)}
  .photo--exam{left:640px;top:615px;width:120px;height:191px;background:linear-gradient(90deg,#5fb3a6,#9bd3ca)}
  .wave{position:absolute;left:0;top:585px;width:760px;height:50px}

  /* right */
  .photo--clinic{left:0;top:0;width:380px;height:180px;background:linear-gradient(120deg,#f3f7f8,#cfe1e6 45%,#eef4f6)}
  .brand{position:absolute;left:40px;top:70px;width:320px;display:flex;align-items:center;gap:12px;font-family:"Cinzel",serif;font-size:20px;letter-spacing:2px;color:var(--teal-deep)}
  .brand-dot{width:24px;height:24px;border-radius:50%;background:var(--teal);flex:none}
  .providers{position:absolute;left:30px;top:192px;width:330px;font-family:"Lora",serif;font-size:12.5px;line-height:1.45}
  .providers h3{font-family:"Lora",serif;font-weight:400;font-size:13.5px;letter-spacing:1px;text-transform:uppercase}
  .photo--map{left:30px;top:338px;width:320px;height:150px;background:#f4f6f6;border:1px solid #d8dede}
  .contact-zone{position:absolute;left:0;top:515px;width:380px;height:291px;background:linear-gradient(180deg,#e6f5f2,#b9e2db)}
  .contact{position:absolute;left:24px;top:50px;width:334px;list-style:none}
  .contact li{display:flex;align-items:center;gap:12px;height:68px;border-bottom:1.5px solid var(--teal-deep);font-family:"Cinzel",serif;font-size:13px;letter-spacing:.8px;line-height:1.35}
  .contact .phone-line{font-size:19px}
  .contact .email-line{font-size:11.5px;letter-spacing:.3px;white-space:nowrap}
  .icon{width:44px;height:44px;border-radius:50%;background:var(--teal);display:flex;align-items:center;justify-content:center;flex:none}
</style>
</head>
<body>
<main class="brochure">

  <section class="panel panel--left">
    <div class="photo photo--toddlers" role="img" aria-label="Two toddlers brushing their teeth"></div>
    <h2 class="band band--child">Child Dental<br>Benefits Schedule</h2>
    <p class="child-copy">A dental benefits program is available for eligible children aged 2 to 17 and will <strong>receive $1000</strong> for dental treatments.</p>
    <p class="child-copy">To check if your children are eligible call us on <span class="phone">9000 4182</span></p>
    <div class="rule" style="left:36px;top:555px;width:310px"></div>
  </section>

  <section class="panel panel--middle">
    <div class="photo photo--smile" role="img" aria-label="Close-up of a smile before and after whitening"></div>
    <h2 class="band band--treat">Dental Treatments</h2>
    <ul class="treatments">
      <li><svg width="18" height="18"><circle cx="9" cy="9" r="7" fill="none" stroke="var(--plum)" stroke-width="1.4"/></svg>Fillings</li>
      <li><svg width="18" height="18"><circle cx="9" cy="9" r="7" fill="none" stroke="var(--plum)" stroke-width="1.4"/></svg>Crowns &amp; Bridges</li>
      <li><svg width="18" height="18"><circle cx="9" cy="9" r="7" fill="none" stroke="var(--plum)" stroke-width="1.4"/></svg>Braces</li>
      <li><svg width="18" height="18"><circle cx="9" cy="9" r="7" fill="none" stroke="var(--plum)" stroke-width="1.4"/></svg>Root Canal Therapy</li>
      <li><svg width="18" height="18"><circle cx="9" cy="9" r="7" fill="none" stroke="var(--plum)" stroke-width="1.4"/></svg>Implants</li>
      <li><svg width="18" height="18"><circle cx="9" cy="9" r="7" fill="none" stroke="var(--plum)" stroke-width="1.4"/></svg>Teeth Extraction</li>
      <li><svg width="18" height="18"><circle cx="9" cy="9" r="7" fill="none" stroke="var(--plum)" stroke-width="1.4"/></svg>Denture</li>
      <li><svg width="18" height="18"><circle cx="9" cy="9" r="7" fill="none" stroke="var(--plum)" stroke-width="1.4"/></svg>Veneer &amp; Cosmetic</li>
    </ul>
    <h2 class="band band--promo">Special Promotions</h2>
    <p class="promo-copy">Gap free dental check-up, clean &amp; x-rays for all health insurances**<br>At home whitening kit now <strong>$199</strong><br>Limited time only (normally $395)</p>
    <div class="rule" style="left:30px;top:526px;width:320px"></div>
    <p class="promo-note">**Conditions apply - Ask staff for more information</p>
  </section>

  <div class="photo photo--kids" role="img" aria-label="Group of smiling children in teal tone"></div>
  <div class="photo photo--exam" role="img" aria-label="Patient with braces during a dental check in teal tone"></div>
  <svg class="wave" viewBox="0 0 760 50" preserveAspectRatio="none" aria-hidden="true">
    <path d="M0 18 C250 40 500 10 760 20 L760 0 L0 0 Z" fill="#ffffff"/>
    <path d="M0 18 C250 40 500 10 760 20 L760 32 C500 22 250 52 0 34 Z" fill="var(--teal-pale)"/>
  </svg>

  <section class="panel panel--right">
    <div class="photo photo--clinic" role="img" aria-label="Softly blurred dentist at work"></div>
    <div class="brand"><span class="brand-dot"></span>Brackenfold Dental Surgery</div>
    <div class="providers">
      <h3>Dental Providers:</h3>
      Dr Mai Tran BDSc (Melb), ICCDE<br>
      Dr Quoc Vu BDSc (Melb), FICCDE, FRACDS, PGradDipCD Implants (Melb)<br>
      Dr Linh Do BHsc Mdent (Latrobe)<br>
      Dr Adam Ngo BHsc Mdent (Latrobe), FRACDS<br>
      Dr Rosa Lam BDS (Adl)
    </div>
    <div class="photo photo--map" role="img" aria-label="Street map showing the clinic location"></div>
    <div class="contact-zone">
      <ul class="contact">
        <li><span class="icon"><svg width="22" height="22" viewBox="0 0 24 24"><path d="M12 2a7 7 0 0 0-7 7c0 5 7 13 7 13s7-8 7-13a7 7 0 0 0-7-7zm0 9.5A2.5 2.5 0 1 1 12 6.5a2.5 2.5 0 0 1 0 5z" fill="#fff"/></svg></span>48 Brackenfold Road, Marrowvale, VIC 3990</li>
        <li class="phone-line"><span class="icon"><svg width="22" height="22" viewBox="0 0 24 24"><path d="M6.6 10.8a15 15 0 0 0 6.6 6.6l2.2-2.2a1 1 0 0 1 1-.25 11.4 11.4 0 0 0 3.6.57 1 1 0 0 1 1 1V20a1 1 0 0 1-1 1A17 17 0 0 1 3 4a1 1 0 0 1 1-1h3.5a1 1 0 0 1 1 1c0 1.25.2 2.45.57 3.6a1 1 0 0 1-.25 1z" fill="#fff"/></svg></span>(03) 9000 4182</li>
        <li class="email-line"><span class="icon"><svg width="22" height="22" viewBox="0 0 24 24"><rect x="3" y="5" width="18" height="14" rx="1.5" fill="none" stroke="#fff" stroke-width="2"/><path d="M3 6l9 7 9-7" fill="none" stroke="#fff" stroke-width="2"/></svg></span>admin@brackenfolddental.com.au</li>
      </ul>
    </div>
  </section>

</main>
</body>
</html>
```